Design Product Packaging For Face Mask Brand

We need packaging designed for a new product, "Harbor Bloom Cover" a made in canada multi layer poly cotton reusable non-medical face mask for all people. The mask ties in the back behind the head.

Preference is a 4x6' flat polybag or 5x7" resealable stand up bag.

We would like to see bold easy to read colour block designs that use the colour pink. The final design should communicate a simple, high fashion, bold fun quality product.

IMG-9732 and 9733 are of the actual product.
Img_9695 and 9786 are our logos.
Vintageladyshoppinggreenmask is an image on our website.
2020-04_VK is the style of image we would like to have on the front of the packaging.
Maskonworldoff is an example of fun cute wording.

Please leave space for upc on the back of the package aswell. Open to your creativity in terms of design but colors must stay the same as brand.

Thank you all for you time and submissions.

Harbor Bloom Cover xoxo

Target Market(s)

Canada/USA civilians, non-health workers

Industry/Entity Type

Fashion

Font styles to use
Sans Serif

Colors
ffffff
feeeee
f9d9e8
eea4c8
e667a6
e34298
86cfc6
33b8a4
87cfc6

Requirements
Must have
• our logo, brand colors, upc on back
Nice to have
• Bold Font
Should not have
• Hard to read handwriting

```html
<!DOCTYPE html>
<html lang="en">
<head>
<meta charset="utf-8">
<title>Harbor Bloom Cover – Resealable Bag Artwork</title>
<link href="https://fonts.googleapis.com/css2?family=Oswald:wght@600&family=Open+Sans:wght@700&display=swap" rel="stylesheet">
<style>
  :root {
    --stage: #d6d6d6;
    --white: #ffffff;
    --teal: #3ab3a1;
    --teal-soft: #cdebe6;
    --blush: #f9eced;
    --rose: #e8898c;
    --rose-soft: #f4c6c8;
  }
  html, body {
    margin: 0;
    padding: 0;
    width: 1200px;
    height: 2176px;
    overflow: hidden;
    background: var(--stage);
  }
  .canvas {
    position: relative;
    width: 1200px;
    height: 2176px;
  }
  .bag-fronts {
    position: absolute;
    top: 540px;
    left: 40px;
    display: flex;
    gap: 40px;
  }
  .bag-front {
    position: relative;
    width: 540px;
    height: 750px;
    overflow: hidden;
  }
  .bag-front--teal { background: var(--white); }
  .bag-front--blush { background: var(--blush); }
  .bag-front svg.wave {
    position: absolute;
    inset: 0;
  }
  .wave-teal { fill: var(--teal); }
  .wave-white { fill: var(--white); }
  .brand-title {
    position: absolute;
    top: 172px;
    left: 300px;
    width: 154px;
    margin: 0;
    font-family: "Oswald", sans-serif;
    font-weight: 600;
    font-size: 36px;
    line-height: 1.0;
    text-align: center;
    color: var(--rose);
    text-transform: uppercase;
    letter-spacing: -0.5px;
  }
  .brand-dot {
    position: absolute;
    top: 178px;
    left: 276px;
    width: 16px;
    height: 16px;
    border-radius: 50%;
    background: var(--rose);
  }
  .mask-art {
    position: absolute;
    top: 320px;
    left: 90px;
    width: 340px;
    height: 310px;
    border-radius: 46% 54% 48% 52% / 40% 46% 54% 60%;
  }
  .bag-front--teal .mask-art { background: var(--teal-soft); }
  .bag-front--blush .mask-art { background: var(--rose-soft); }
  .brand-signoff {
    position: absolute;
    top: 612px;
    left: 312px;
    display: flex;
    align-items: center;
    gap: 6px;
    font-family: "Oswald", sans-serif;
    font-weight: 600;
    font-size: 12px;
    color: var(--rose);
    text-transform: uppercase;
    white-space: nowrap;
  }
  .brand-signoff::before {
    content: "";
    width: 10px;
    height: 10px;
    border-radius: 50%;
    background: var(--rose);
  }
  .spec-caption {
    position: absolute;
    top: 1400px;
    left: 0;
    width: 1200px;
    margin: 0;
    font-family: "Open Sans", sans-serif;
    font-weight: 700;
    color: var(--white);
    text-align: center;
    letter-spacing: 0.32em;
  }
  .spec-caption span { display: block; }
  .spec-caption .spec-mood { font-size: 42px; line-height: 60px; }
  .spec-caption .spec-size { font-size: 42px; line-height: 60px; }
  .spec-caption .spec-type { font-size: 36px; line-height: 56px; }
</style>
</head>
<body>
<main class="canvas">
  <section class="bag-fronts">
    <article class="bag-front bag-front--teal">
      <svg class="wave" width="540" height="750" viewBox="0 0 540 750" aria-hidden="true">
        <path class="wave-teal" d="M368,0 C300,40 250,90 254,150 C258,260 380,330 430,420 C470,500 460,640 372,750 L540,750 L540,0 Z"/>
      </svg>
      <span class="brand-dot"></span>
      <h2 class="brand-title">Harbor<br>Bloom<br>Cover</h2>
      <div class="mask-art" role="img" aria-label="Teal line drawing of a tie-back cloth face mask"></div>
      <p class="brand-signoff">Harbor Bloom Cover</p>
    </article>
    <article class="bag-front bag-front--blush">
      <svg class="wave" width="540" height="750" viewBox="0 0 540 750" aria-hidden="true">
        <path class="wave-white" d="M368,0 C300,40 250,90 254,150 C258,260 380,330 430,420 C470,500 460,640 372,750 L540,750 L540,0 Z"/>
      </svg>
      <span class="brand-dot"></span>
      <h2 class="brand-title">Harbor<br>Bloom<br>Cover</h2>
      <div class="mask-art" role="img" aria-label="Pink line drawing of a tie-back cloth face mask"></div>
      <p class="brand-signoff">Harbor Bloom Cover</p>
    </article>
  </section>
  <p class="spec-caption">
    <span class="spec-mood">SIMPLE , BOLD, PLAYFUL</span>
    <span class="spec-size">5INCH X 7 INCH</span>
    <span class="spec-type">RESEALABLE BAG</span>
  </p>
</main>
</body>
</html>
```